Velvet Lantern rebranding my business with a new business card

I have my new logo and now I need a refresher on my business cards. I really want something fun and fresh. I like black background or anything to make the color pop.
Logo
Name: Velvet Lantern
Contact Info as stated below:
Mara Pelkin
519-555-0147
Logo
Name: Velvet Lantern
Mara Pelkin
519-555-0147
fb.me/VelvetLanternbyMara
Instagram: @VelvetLanternbyMara

Industry/Entity Type

Business

Contact Information for Business Card

double-sided. Logo on one side. Contact info on the other.

Requirements
Must have
• Logo
• Name: Velvet Lantern
• Contact Info as stated below:
• Mara Pelkin
• 519-555-0147
• fb.me/VelvetLanternbyMara
• fb.me/VelvetLanternbyMara

```html
<!DOCTYPE html>
<html lang="en">
<head>
<meta charset="utf-8">
<title>Velvet Lantern — Business Card</title>
<link rel="stylesheet" href="https://fonts.googleapis.com/css2?family=Source+Sans+3:wght@400;600&display=swap">
<style>
  :root {
    --backdrop: #2b2b2d;
    --card-base: #231f20;
    --band-dark: #191718;
    --accent-pink: #c04d96;
    --ink-light: #f4f1f3;
    --badge-white: #ffffff;
    --badge-ink: #2a2326;
  }
  * { box-sizing: border-box; margin: 0; padding: 0; }
  html, body {
    width: 1200px;
    height: 1200px;
    overflow: hidden;
    background: var(--backdrop);
    font-family: "Source Sans 3", "Myriad Pro", sans-serif;
  }
  .canvas {
    position: relative;
    width: 1200px;
    height: 1200px;
  }
  .card {
    position: absolute;
    left: 249px;
    width: 702px;
    height: 401px;
    overflow: hidden;
    background: var(--card-base);
  }
  .card--front { top: 149px; }
  .card--back { top: 650px; }
  .card__bands {
    position: absolute;
    inset: 0;
    width: 100%;
    height: 100%;
  }
  .band--pink { fill: var(--accent-pink); }
  .band--dark { fill: var(--band-dark); }

  .logo-badge {
    position: absolute;
    left: 50px;
    top: 71px;
    width: 258px;
    height: 258px;
    border-radius: 50%;
    background: var(--badge-white);
    display: flex;
    align-items: center;
    justify-content: center;
  }
  .logo-badge__name {
    font-size: 30px;
    font-weight: 600;
    color: var(--badge-ink);
    text-align: center;
    line-height: 1.1;
  }

  .contact {
    position: absolute;
    left: 340px;
    top: 130px;
    color: var(--ink-light);
  }
  .contact__name {
    font-size: 32px;
    font-weight: 400;
    letter-spacing: 0.2px;
    margin-bottom: 22px;
  }
  .contact__row {
    display: flex;
    align-items: center;
    height: 30px;
    margin-bottom: 13px;
    font-size: 20px;
    font-weight: 400;
  }
  .contact__icon {
    width: 22px;
    height: 30px;
    margin-right: 12px;
    flex: none;
  }
  .contact__dot {
    width: 22px;
    height: 22px;
    margin-right: 12px;
    border-radius: 50%;
    background: var(--accent-pink);
    flex: none;
  }

  .back-mark {
    position: absolute;
    left: 408px;
    top: 201px;
    transform: translate(-50%, -50%);
    font-size: 46px;
    font-weight: 600;
    color: var(--ink-light);
    white-space: nowrap;
  }
</style>
</head>
<body>
<main class="canvas">

  <section class="card card--front" aria-label="Business card, contact side">
    <svg class="card__bands" viewBox="0 0 614 351" preserveAspectRatio="none" aria-hidden="true">
      <polygon class="band--dark" points="67,0 167,0 -38,351 -138,351"/>
      <polygon class="band--pink" points="0,0 67,0 0,115"/>
      <polygon class="band--pink" points="167,0 272,0 67,351 -38,351"/>
      <polygon class="band--pink" points="614,175 614,351 512,351"/>
    </svg>

    <div class="logo-badge">
      <span class="logo-badge__name">Velvet<br>Lantern</span>
    </div>

    <div class="contact">
      <p class="contact__name">Mara Pelkin</p>
      <p class="contact__row">
        <svg class="contact__icon" viewBox="0 0 22 30" aria-hidden="true">
          <rect x="3" y="1.5" width="16" height="27" rx="3" fill="none" stroke="#c04d96" stroke-width="2"/>
          <line x1="3" y1="6" x2="19" y2="6" stroke="#c04d96" stroke-width="1.5"/>
          <line x1="3" y1="23" x2="19" y2="23" stroke="#c04d96" stroke-width="1.5"/>
          <circle cx="11" cy="25.8" r="1.2" fill="#c04d96"/>
        </svg>
        519-555-0147
      </p>
      <p class="contact__row">
        <span class="contact__dot" aria-hidden="true"></span>
        VelvetLanternbyMara
      </p>
    </div>
  </section>

  <section class="card card--back" aria-label="Business card, logo side">
    <svg class="card__bands" viewBox="0 0 614 351" preserveAspectRatio="none" aria-hidden="true">
      <polygon class="band--dark" points="67,0 167,0 -38,351 -138,351"/>
      <polygon class="band--pink" points="0,0 67,0 0,115"/>
      <polygon class="band--pink" points="167,0 272,0 67,351 -38,351"/>
      <polygon class="band--pink" points="614,175 614,351 512,351"/>
    </svg>
    <p class="back-mark">Velvet Lantern</p>
  </section>

</main>
</body>
</html>
```